Simple, elegant, business card design required

Hi designers,I am looking for a simple yet elegant business card design.

Please make use of my logo (attached); you are free to tweak the logo should you wish to do so.

Our business is involved in many different fields - almost all of them involved in some form of "design", so that's really one of the key things I want to portray. I do not wish to specify which field of design, exactly.

I prefer white on black (or just monochromatic), but if you have a different, creative idea, I am open to that too.

You can use artsy photographs provided that you have the license to use those. Please feel free to ask me any questions.
Updates

Project Deadline Extended Reason: Small extension for potential revisions. Did not get the time to provide as much feedback as I can. Added Wednesday, July 09, 2014

Target Market(s)

High-end customers looking for design consultancy

Industry/Entity Type

Business

Contact Information for Business Card

Name: Gareth Moonfield
Position: Creative Director
Mobile: +155603928174
Address: Barrow Lane, Hollinbridge upon Avel, Wendmarsh GL12 4RT
Website: torvakest.com (not launched yet)

Requirements
Must have
• Design layout must be clean, original, and text must be readable when printed.
Should not have
• ~ No business card templates please. Anyone using this will be reported.
• ~ Please don't spam entries.

```html
<!DOCTYPE html>
<html lang="en">
<head>
<meta charset="utf-8">
<title>Torvakest – Business Card</title>
<link rel="stylesheet" href="https://fonts.googleapis.com/css2?family=Jost:wght@300;400&family=Cabin:wght@600&display=swap">
<style>
  :root {
    --ink: #231f20;
    --paper: #ffffff;
    --facet-dark: #1c1c1e;
    --facet-mid: #55565a;
    --facet-light: #8a8688;
  }
  * { margin: 0; padding: 0; box-sizing: border-box; }
  html, body {
    width: 1200px;
    height: 691px;
    overflow: hidden;
    background: var(--paper);
  }
  .card {
    position: relative;
    width: 1200px;
    height: 691px;
    background: var(--paper);
    font-family: "Jost", sans-serif;
    color: var(--paper);
  }
  .header-band {
    position: absolute;
    left: 0; top: 0;
    width: 1200px; height: 227px;
    background: var(--ink);
  }
  .brand-plate {
    position: absolute;
    left: 407px; top: 0;
    width: 440px; height: 227px;
    display: flex;
    align-items: center;
    justify-content: center;
    background: var(--paper);
  }
  .brand-name {
    font-family: "Jost", sans-serif;
    font-weight: 400;
    font-size: 64px;
    letter-spacing: 12px;
    padding-left: 12px;
    color: var(--ink);
    line-height: 1;
  }
  .facet-field {
    position: absolute;
    left: 0;
    width: 1200px;
    background:
      linear-gradient(115deg, var(--facet-dark) 0%, var(--facet-mid) 30%, var(--facet-dark) 55%, var(--facet-mid) 75%, var(--facet-light) 100%);
  }
  .facet-field--main { top: 240px; height: 366px; }
  .facet-field--foot { top: 634px; height: 57px; }
  .identity {
    position: absolute;
    right: 754px;
    top: 344px;
    text-align: right;
  }
  .person-name {
    font-family: "Cabin", sans-serif;
    font-weight: 600;
    font-size: 48px;
    line-height: 1;
  }
  .person-role {
    font-family: "Cabin", sans-serif;
    font-weight: 600;
    font-size: 29px;
    line-height: 1;
    margin-top: 4px;
  }
  .divider {
    position: absolute;
    left: 462px; top: 318px;
    width: 13px; height: 231px;
    background: var(--paper);
  }
  .contact {
    position: absolute;
    left: 490px;
    top: 320px;
    font-weight: 300;
    font-size: 31px;
    line-height: 1.22;
    letter-spacing: 0.5px;
  }
  .contact-phone { font-size: 34px; }
  .contact-address { margin-top: 22px; }
  .contact-web { margin-top: 30px; font-size: 30px; }
</style>
</head>
<body>
  <div class="card">
    <div class="header-band"></div>
    <div class="brand-plate">
      <span class="brand-name">TORVAKEST</span>
    </div>

    <div class="facet-field facet-field--main" role="img" aria-label="Monochrome low-poly faceted background in black and grey"></div>
    <div class="facet-field facet-field--foot" role="img" aria-label="Monochrome low-poly faceted background strip"></div>

    <div class="identity">
      <div class="person-name">Gareth Moonfield</div>
      <div class="person-role">creative director</div>
    </div>

    <div class="divider"></div>

    <div class="contact">
      <div class="contact-phone">+155603928174</div>
      <div class="contact-address">Barrow Lane, Hollinbridge upon Avel,<br>Wendmarsh GL12 4RT</div>
      <div class="contact-web">www.torvakest.com</div>
    </div>
  </div>
</body>
</html>
```